Professional Financial services company want to rebrand their stationary

We need stationary design for Velmor Group, its a company with 4 member companys that include Velmor Auditing, Velmor Financial Consultancy, Velmor Debt Collection and Velmor Real Estate.

We are based in dubai so the designers need to keep in mind that we use both english and arabic so leave a space for the arabic writing.

We recently redesigned our Logo and would like to redesign our stationary to go along with it.

You will find attached the logo, please keep it looking professional and use the logo as a guide for colors when designing.

Good luck to everyone

Industry/Entity Type

Finance And Accounting

Font styles to use
Sans Serif

Colors
0292cd
33a6d7
3276b5
0355a3
ffffff
dbdbdb

Requirements
Must have
• Letterhead
• Business card
• Envelope small and A4
Nice to have
• Professional
• Space for Arabic and english

```html
<!DOCTYPE html>
<html lang="en">
<head>
<meta charset="utf-8">
<title>Velmor Group – Business Card</title>
<link href="https://fonts.googleapis.com/css2?family=Roboto:wght@400;500;700&family=Roboto+Condensed:wght@400;700&family=Noto+Sans+Arabic:wght@400;600;700&display=swap" rel="stylesheet">
<style>
  :root {
    --backdrop: #2b2b2b;
    --brand-blue: #0b6fc0;
    --card-white: #f4f4f4;
    --ink-grey: #5b5b5b;
    --ink-dark: #4a4a4a;
    --rule: #6d6d6d;
    --white: #ffffff;
  }
  * { margin: 0; padding: 0; box-sizing: border-box; }
  html, body {
    width: 1200px; height: 960px; overflow: hidden;
    background: var(--backdrop);
  }
  .canvas { position: relative; width: 1200px; height: 960px; }

  .card { position: absolute; width: 600px; height: 343px; }

  /* Back of card */
  .card-back {
    left: 320px; top: 110px;
    background: var(--brand-blue);
    color: var(--white);
    font-family: "Roboto", Arial, sans-serif;
    text-align: center;
  }
  .card-back .brand-name {
    position: absolute; left: 0; right: 0; top: 132px;
    font-size: 36px; font-weight: 500; letter-spacing: 1px;
  }
  .card-back .members-title {
    position: absolute; left: 0; right: 0; top: 257px;
    font-size: 14px; font-weight: 700;
  }
  .card-back .members-list {
    position: absolute; left: 0; right: 0; top: 282px;
    font-size: 14.5px; line-height: 20px;
  }
  .dot {
    display: inline-block; width: 8px; height: 8px; border-radius: 50%;
    background: var(--white); margin: 0 4px 1px 6px; vertical-align: middle;
  }

  /* Front of card */
  .card-front {
    left: 320px; top: 492px;
    background: var(--card-white);
    font-family: "Roboto", Arial, sans-serif;
  }
  .card-front .brand-name {
    position: absolute; right: 44px; top: 60px;
    font-size: 33px; font-weight: 500; color: var(--brand-blue);
    letter-spacing: 0.5px;
  }
  .person-en { position: absolute; left: 36px; top: 168px; }
  .person-en .name {
    font-family: "Roboto Condensed", Arial, sans-serif;
    font-size: 22px; font-weight: 700; color: var(--brand-blue); line-height: 26px;
  }
  .person-en .role {
    font-size: 14.5px; font-weight: 500; color: var(--ink-grey); letter-spacing: 0.3px;
  }
  .person-ar {
    position: absolute; right: 38px; top: 158px; text-align: right; direction: rtl;
    font-family: "Noto Sans Arabic", Arial, sans-serif;
  }
  .person-ar .name { font-size: 24px; font-weight: 700; color: var(--brand-blue); line-height: 30px; }
  .person-ar .role { font-size: 17px; font-weight: 600; color: var(--ink-grey); line-height: 20px; }

  .divider {
    position: absolute; left: 36px; right: 38px; top: 221px;
    height: 1px; background: var(--rule);
  }
  .address-en {
    position: absolute; left: 36px; top: 229px;
    font-size: 14.5px; line-height: 18px; color: var(--ink-dark);
  }
  .address-ar {
    position: absolute; left: 36px; top: 272px; direction: rtl; text-align: left;
    font-family: "Noto Sans Arabic", Arial, sans-serif;
    font-size: 13.5px; line-height: 23px; color: var(--ink-dark);
  }
  .address-ar span { display: block; text-align: left; direction: rtl; unicode-bidi: plaintext; }

  .contact-list {
    position: absolute; right: 38px; top: 226px; list-style: none;
    font-size: 14.5px; color: var(--ink-dark);
  }
  .contact-list li {
    display: flex; justify-content: flex-end; align-items: center;
    height: 19px; gap: 8px;
  }
  .contact-list svg { width: 13px; height: 13px; fill: var(--brand-blue); flex: none; }
</style>
</head>
<body>
<main class="canvas">

  <section class="card card-back" aria-label="Card back">
    <div class="brand-name">VELMOR GROUP</div>
    <div class="members-title">MEMBER COMPANIES</div>
    <div class="members-list">
      Velmor Auditing <span class="dot"></span>Velmor Financial Consultancy<br>
      Velmor Debt Collection<span class="dot"></span>Velmor Real Estate
    </div>
  </section>

  <section class="card card-front" aria-label="Card front">
    <div class="brand-name">VELMOR GROUP</div>

    <div class="person-en">
      <div class="name">SAMER HADDAD</div>
      <div class="role">CEO/FOUNDER</div>
    </div>
    <div class="person-ar" lang="ar">
      <div class="name">سامر حداد</div>
      <div class="role">مؤسس</div>
    </div>

    <div class="divider"></div>

    <address class="address-en" style="font-style:normal">
      214 Coral Bay Road<br>
      Port Wren, Marlow 61208
    </address>
    <address class="address-ar" lang="ar" style="font-style:normal">
      <span>214 طريق خليج المرجان</span>
      <span>بورت رين، مارلو 61208</span>
    </address>

    <ul class="contact-list">
      <li>614 302 7185
        <svg viewBox="0 0 16 16" aria-hidden="true"><path d="M3.6 1.2l2.3 2.6-1.2 1.9c.9 2 2.5 3.6 4.6 4.6l1.9-1.2 2.6 2.3-1.3 2.4C7.4 13.6 2.4 8.6 1.2 3.5z"/></svg></li>
      <li>742 519 0836
        <svg viewBox="0 0 16 16" aria-hidden="true"><path d="M4.5 0h7a1 1 0 011 1v14a1 1 0 01-1 1h-7a1 1 0 01-1-1V1a1 1 0 011-1zm.8 2v10.5h5.4V2zM8 13.3a.9.9 0 100 1.8.9.9 0 000-1.8z"/></svg></li>
      <li>538 270 4611
        <svg viewBox="0 0 16 16" aria-hidden="true"><path d="M4 1h8v4H4zM1 6h14v7h-3v2H4v-2H1zm4 5v3h6v-3z"/></svg></li>
      <li>hello@velmorgrp.com
        <svg viewBox="0 0 16 16" aria-hidden="true"><path d="M1 3h14v1.2L8 8.6 1 4.2zm0 2.8l7 4.4 7-4.4V13H1z"/></svg></li>
      <li>www.velmorgrp.com
        <svg viewBox="0 0 16 16" aria-hidden="true"><path d="M8 1a7 7 0 110 14A7 7 0 018 1zm-2 3.2L4.2 5.5l1 2.3 2 .6.3 2.2 1.5 1.6.6-2.4 1.7-1-1-1.8-2.2-.3-.4-1.7z"/></svg></li>
    </ul>
  </section>

</main>
</body>
</html>
```